Cover for Where the Quiet River Bends Beyond Our Morning

Cover for a book that describes everything that happens to a person, from pre-birth life plans through growing in compassion and wisdom to death and living in the afterlife. The information is revealed in messages from people living in the life after this life. The title is Lanterns Along the Hidden Stair of Every Soul: Gathered from Voices Dwelling in the Further Meadow. Author is T. Morven Ashdale. Book size is 6 by 9.

Target Market(s)

General

Font styles to use
Serif

```html
<!DOCTYPE html>
<html lang="en">
<head>
<meta charset="utf-8">
<title>Lanterns Along the Hidden Stair of Every Soul — Book Cover</title>
<link rel="stylesheet" href="https://fonts.googleapis.com/css2?family=Marcellus&display=swap">
<style>
  :root {
    --stage: #d6d6d6;
    --paper: #ececec;
    --paper-light: #f3f3f3;
    --ink: #1c1c1c;
    --accent: #b31b1f;
    --placeholder: #c9c9c9;
  }
  * { margin: 0; padding: 0; box-sizing: border-box; }
  html, body {
    width: 989px;
    height: 1200px;
    overflow: hidden;
    background: var(--stage);
  }
  .cover {
    position: absolute;
    left: 69.5px;
    top: 0;
    width: 850px;
    height: 1200px;
    background: radial-gradient(ellipse at 50% 35%, var(--paper-light) 0%, var(--paper) 60%, #e4e4e4 100%);
    font-family: "Marcellus", serif;
    color: var(--ink);
    text-align: center;
  }
  .author {
    position: absolute;
    top: 66px;
    left: 0;
    right: 0;
    font-size: 30px;
    line-height: 36px;
    letter-spacing: 0.01em;
    text-transform: uppercase;
  }
  .illustration {
    position: absolute;
    left: 87px;
    top: 421px;
    width: 661px;
    height: 129px;
    background: var(--placeholder);
  }
  .title-main {
    position: absolute;
    top: 797px;
    left: 0;
    right: 0;
    font-size: 104px;
    font-weight: 400;
    line-height: 1;
    letter-spacing: 0.05em;
    color: var(--accent);
    text-transform: uppercase;
  }
  .title-sub {
    position: absolute;
    top: 910px;
    left: 0;
    right: 0;
    font-size: 42px;
    line-height: 46px;
    text-transform: uppercase;
  }
  .tagline {
    position: absolute;
    top: 1112px;
    left: 0;
    right: 0;
    font-size: 21px;
    line-height: 26px;
    text-transform: uppercase;
    letter-spacing: -0.01em;
  }
</style>
</head>
<body>
  <main class="cover">
    <p class="author">T. Morven Ashdale</p>
    <div class="illustration" role="img" aria-label="Illustration of a row of toppling dominoes, the first one red and the rest black"></div>
    <h1 class="title-main">Lanterns</h1>
    <p class="title-sub">Along the Hidden Stair<br>of Every Soul</p>
    <p class="tagline">Gathered from Voices Dwelling in the Further Meadow</p>
  </main>
</body>
</html>
```